Ferndale Chapel of Grace (this will be used for new church sign) sign will be 4'x8' and would like also listed Sunday School 9:00am Worship Service 10:30am.

Logo Text

FERNDALE CHAPEL OF GRACE

```html
<!DOCTYPE html>
<html lang="en">
<head>
<meta charset="utf-8">
<title>Ferndale Chapel of Grace – Church Sign</title>
<link rel="stylesheet" href="https://fonts.googleapis.com/css2?family=Anton&family=Poppins:wght@400;600;700;800&display=swap">
<style>
  :root{
    --crimson:#c41e4a;
    --gold:#c9ac06;
    --ink:#0d0d0d;
    --paper:#ffffff;
    --backdrop:#b7b7b7;
  }
  *{margin:0;padding:0;box-sizing:border-box}
  html,body{width:800px;height:1200px;overflow:hidden;background:var(--backdrop)}
  .canvas{position:relative;width:800px;height:1200px}
  .sign{
    position:absolute;left:20px;top:410px;width:760px;height:380px;
    background:var(--paper);overflow:hidden;
    border-bottom:2px solid var(--crimson);
    box-shadow:6px 10px 14px rgba(0,0,0,.35);
    font-family:'Poppins',sans-serif;
  }
  .brand-dot{position:absolute;left:32px;top:50px;width:50px;height:50px;border-radius:50%;background:var(--gold)}
  .brand-name{position:absolute;left:92px;top:100px;font-weight:800;font-size:19px;line-height:1;color:var(--crimson);white-space:nowrap}
  .title-main{position:absolute;left:20px;top:166px;font-family:'Anton',sans-serif;font-weight:400;font-size:76px;line-height:1;color:var(--ink);letter-spacing:1px;white-space:nowrap}
  .title-sub{position:absolute;left:20px;top:240px;font-weight:800;font-size:35px;line-height:1;color:var(--crimson);white-space:nowrap}
  .address{position:absolute;left:20px;top:290px;display:flex;align-items:center}
  .address-pin{width:22px;height:28px;position:relative;z-index:1}
  .address-bar{background:var(--gold);height:27px;width:318px;margin-left:-6px;padding-left:14px;display:flex;align-items:center;font-weight:600;font-size:12.5px;color:var(--ink);white-space:nowrap}
  .website{position:absolute;left:20px;top:331px;font-weight:700;font-size:15px;letter-spacing:1.6px;color:var(--ink);white-space:nowrap}
  .website span{color:var(--crimson)}
  .schedule{position:absolute;left:0;top:0;width:760px;height:380px}
  .schedule text{font-family:'Poppins',sans-serif;text-anchor:middle}
  .hd{fill:var(--paper);font-weight:800}
  .lbl{fill:var(--ink);font-weight:800;font-size:20px}
  .time{fill:var(--paper);font-weight:800;font-size:21px}
</style>
</head>
<body>
<div class="canvas">
  <section class="sign">
    <svg class="schedule" viewBox="0 0 760 380" aria-label="Service schedule">
      <defs>
        <clipPath id="inner-disc"><circle cx="578" cy="190" r="165"/></clipPath>
        <linearGradient id="arch-tone" x1="0" y1="0" x2="0" y2="1">
          <stop offset="0" stop-color="#b01a44"/>
          <stop offset="1" stop-color="#cc2350"/>
        </linearGradient>
        <linearGradient id="arch-gold" x1="0" y1="0" x2="0" y2="1">
          <stop offset="0" stop-color="#d2b40a"/>
          <stop offset="1" stop-color="#bfa204"/>
        </linearGradient>
      </defs>
      <circle cx="569" cy="190" r="196" fill="url(#arch-tone)" role="img" aria-label="Church interior with gothic arches, tinted crimson"/>
      <g clip-path="url(#inner-disc)">
        <rect x="400" y="20" width="360" height="360" fill="url(#arch-gold)" role="img" aria-label="Church interior with gothic arches, tinted gold"/>
        <rect x="400" y="213" width="360" height="33" fill="var(--crimson)"/>
        <rect x="400" y="284" width="360" height="34" fill="var(--crimson)"/>
      </g>
      <text class="hd" x="578" y="119" font-size="37" textLength="248" lengthAdjust="spacingAndGlyphs">DISCIPLESHIP</text>
      <text class="hd" x="578" y="162" font-size="55" textLength="248" lengthAdjust="spacingAndGlyphs">CLASSES</text>
      <line x1="544" y1="180" x2="613" y2="180" stroke="#fff" stroke-width="1.5"/>
      <text class="lbl" x="578" y="207" textLength="217" lengthAdjust="spacingAndGlyphs">SUNDAY SCHOOL</text>
      <text class="time" x="578" y="239" textLength="96" lengthAdjust="spacingAndGlyphs">9:00AM</text>
      <text class="lbl" x="578" y="279" textLength="229" lengthAdjust="spacingAndGlyphs">WORSHIP SERVICE</text>
      <text class="time" x="578" y="311" textLength="107" lengthAdjust="spacingAndGlyphs">10:30AM</text>
    </svg>

    <span class="brand-dot"></span>
    <span class="brand-name">Ferndale Chapel of Grace</span>

    <h1>
      <span class="title-main">FERNDALE</span>
      <span class="title-sub">CHAPEL OF GRACE</span>
    </h1>

    <div class="address">
      <svg class="address-pin" viewBox="0 0 22 28" aria-hidden="true">
        <path d="M11 1C5.5 1 1.5 5 1.5 10.3 1.5 17 11 27 11 27s9.5-10 9.5-16.7C20.5 5 16.5 1 11 1z" fill="var(--crimson)"/>
        <circle cx="11" cy="10.3" r="4" fill="#fff"/>
      </svg>
      <div class="address-bar">48 Willow Bend Road, Ferndale, OR 97410</div>
    </div>

    <p class="website">www.<span>ferndalechapelofgrace</span>.com</p>
  </section>
</div>
</body>
</html>
```